Cedar Hollow Athletic Director Business Cards

I am the AD/Head Football Coach of Mesa Verdin CISD in Texas. I want a fully colored design front and back that really pops. I will include a few pictures. Dark Maroon and Vegas Gold are our colors and we are the badgers. I would like the card to have a picture of our mascot on the front with my info and a dark maroon back with our helmet in white and vegas gold (helmet decal I included)

Target Market(s)

Other head athletic coaches and Athletic Directors, principals and superintendents

Industry/Entity Type

Business

Contact Information for Business Card

Dwayne Kettler
Athletic Director/Head Football Coach
Cedar Hollow CISD
412 S. Willet Ave.
Cedar Hollow Texas 78419
Office - (956) 318-7260
Cell - (956) 372-8154

Font styles to use
Serif

Requirements
Must have
• Football helmet like the ones included. Fully colored double sided. Varo Dark Maroon and Vegas Gold main colors.
Nice to have
• One of the pictures I included on the back of card.

```html
<!DOCTYPE html>
<html lang="en">
<head>
<meta charset="utf-8">
<title>Cedar Hollow CISD – Athletic Director Business Card</title>
<link rel="stylesheet" href="https://fonts.googleapis.com/css2?family=Lato:wght@400;700;900&display=swap">
<style>
  :root {
    --maroon: #5a1a1a;
    --maroon-text: #6e1c22;
    --gold: #c9a227;
    --ink: #1d1d1d;
    --paper: #ffffff;
    --backdrop: #e9e6e1;
    --turf: #5d7a45;
    --helmet-white: #d9dbd6;
  }
  * { box-sizing: border-box; margin: 0; padding: 0; }
  html, body { width: 1200px; height: 901px; overflow: hidden; }
  body {
    background: var(--backdrop);
    font-family: "Lato", sans-serif;
    color: var(--ink);
    display: flex;
    flex-direction: column;
    align-items: center;
    justify-content: center;
    gap: 34px;
  }
  .card {
    position: relative;
    width: 700px;
    height: 400px;
    background: var(--paper);
    overflow: hidden;
    box-shadow: 0 6px 18px rgba(0,0,0,.18);
  }
  .card-back .photo {
    position: absolute; inset: 0;
    background: linear-gradient(100deg, var(--turf) 0%, var(--turf) 35%, var(--helmet-white) 100%);
  }
  .brand {
    position: absolute;
    left: 60px; top: 52px;
    display: flex; align-items: center; gap: 14px;
    font-weight: 900;
    font-size: 26px;
    color: var(--maroon-text);
  }
  .brand-dot {
    width: 46px; height: 46px;
    border-radius: 50%;
    background: var(--gold);
  }
  .address {
    position: absolute;
    left: 44px; top: 168px;
    font-size: 19px;
    line-height: 1.3;
    font-style: normal;
  }
  .identity {
    position: absolute;
    right: 44px; top: 168px;
    text-align: right;
  }
  .identity .name {
    font-size: 31px;
    font-weight: 900;
    color: var(--maroon-text);
    line-height: 1.1;
  }
  .identity .title {
    font-size: 19px;
    margin-top: 4px;
  }
  .contact {
    position: absolute;
    right: 60px; top: 262px;
    list-style: none;
    font-size: 20px;
    line-height: 1.3;
  }
  .contact li { display: flex; align-items: center; gap: 10px; }
  .contact svg { width: 16px; height: 16px; fill: var(--maroon-text); }
  .swoosh { position: absolute; inset: 0; width: 100%; height: 100%; }
</style>
</head>
<body>

  <section class="card card-back" aria-label="Card back">
    <div class="photo" role="img" aria-label="Team photograph: white football helmets resting on green turf"></div>
  </section>

  <section class="card card-front" aria-label="Card front">
    <svg class="swoosh" viewBox="0 0 700 400" preserveAspectRatio="none" aria-hidden="true">
      <path d="M0,262 C190,320 440,368 700,388 L700,400 L0,400 Z" fill="var(--maroon)"/>
      <path d="M0,247 C190,305 440,352 700,374" fill="none" stroke="var(--gold)" stroke-width="9"/>
    </svg>

    <div class="brand"><span class="brand-dot"></span>Cedar Hollow Badgers</div>

    <address class="address">
      Cedar Hollow CISD<br>
      412 S. Willet Ave.<br>
      Cedar Hollow Texas 78419
    </address>

    <div class="identity">
      <p class="name">Dwayne Kettler</p>
      <p class="title">Athletic Director / Head Football Coach</p>
    </div>

    <ul class="contact">
      <li>
        <svg viewBox="0 0 24 24" aria-label="Office"><path d="M6.6 10.8a15.1 15.1 0 0 0 6.6 6.6l2.2-2.2a1 1 0 0 1 1-.25 11.4 11.4 0 0 0 3.6.57 1 1 0 0 1 1 1V20a1 1 0 0 1-1 1A17 17 0 0 1 3 4a1 1 0 0 1 1-1h3.5a1 1 0 0 1 1 1c0 1.250.2 2.450.57 3.6a1 1 0 0 1-.25 1z"/></svg>
        (956) 318-7260
      </li>
      <li>
        <svg viewBox="0 0 24 24" aria-label="Cell"><path d="M7 2h10a2 2 0 0 1 2 2v16a2 2 0 0 1-2 2H7a2 2 0 0 1-2-2V4a2 2 0 0 1 2-2zm0 3v9h10V5zm2 11v2h2v-2zm4 0v2h2v-2z"/></svg>
        (956) 372-8154
      </li>
    </ul>
  </section>

</body>
</html>
```